Job advert for Forged Here Collective

I would like a poster graphic that I can promote on social media to advertise a job vacancy we will be promoting our upcoming jobs, here is the text...

WE ARE ON THE…

LOOKOUT
(maybe insert graphic or icon that fits with the message here)

For A

OPERATIONS AND HR MANAGER

MEMBERSHIP ADVISOR (EAST MIDLANDS)

SOCIAL MEDIA CONTENT CREATOR

THE UK’s FASTEST GROWING NETWORK FOR MANUFACTURERS

OFFICES IN BIRMINGHAM AND LEEDS - WE ARE AN INCLUSIVE EMPLOYER (use the equality logo provided here)

Target Market(s)

people looking to find a new job

Industry/Entity Type

Manufacture

Font styles to use
Sans Serif

Colors
f04a50
f68e4e
e667a6

Requirements
Must have
• Clear simple and contemporary style
Nice to have
• a nice graphic or icon to convey the text message
Should not have
• use of dark depressing colours

```html
<!DOCTYPE html>
<html lang="en">
<head>
<meta charset="utf-8">
<title>Forged Here Collective – We Are On The Lookout</title>
<link rel="stylesheet" href="https://fonts.googleapis.com/css2?family=Bebas+Neue&family=Montserrat:wght@600;700&display=swap">
<style>
  :root{
    --pink:#e667a6;
    --pink-light:#f6c3dc;
    --red:#f04a50;
    --orange:#f68e4e;
    --ink:#111111;
    --white:#ffffff;
    --stage:#e4e4e4;
    --green:#9bc53d;
  }
  *{margin:0;padding:0;box-sizing:border-box}
  html,body{width:1200px;height:902px;overflow:hidden;background:var(--stage)}
  .poster{
    position:absolute;left:296px;top:21px;width:608px;height:860px;
    overflow:hidden;background:var(--white);
    font-family:"Montserrat",Arial,sans-serif;
  }
  .poster-art{position:absolute;inset:0}
  .headline{position:absolute;font-family:"Bebas Neue",Impact,sans-serif;color:var(--ink);line-height:1}
  .headline--intro{left:56px;top:112px;font-size:44px}
  .headline--lookout{left:50px;top:146px;font-size:150px;letter-spacing:1px}
  .headline--for{left:484px;top:168px;font-size:40px}
  .vacancies{position:absolute;left:78px;top:340px;list-style:none}
  .vacancy{
    display:flex;align-items:flex-start;gap:12px;margin-bottom:26px;
    font-family:"Bebas Neue",Impact,sans-serif;font-size:33px;line-height:.95;
    color:var(--white);text-shadow:2px 2px 0 var(--ink),-1px -1px 0 var(--ink),1px -1px 0 var(--ink),-1px 1px 0 var(--ink);
  }
  .vacancy-icon{width:18px;height:26px;flex:none;margin-top:6px}
  .tagline{position:absolute;right:34px;top:640px;font-size:12px;font-weight:700;color:var(--ink);letter-spacing:.2px}
  .offices{position:absolute;right:34px;top:668px;text-align:right;font-size:12px;font-weight:700;color:var(--ink);line-height:1.5}
  .partners{position:absolute;right:60px;top:724px;display:flex;gap:48px;align-items:center}
  .partner-badge{width:30px;height:30px;border-radius:50%}
  .partner-badge--green{background:var(--green)}
  .partner-badge--red{background:var(--red)}
  .inclusion-badge{position:absolute;left:46px;top:740px;width:96px;height:96px;border-radius:50%;background:var(--orange)}
</style>
</head>
<body>
<main class="poster">
  <svg class="poster-art" viewBox="0 0 608 860" aria-hidden="true">
    <defs>
      <radialGradient id="pinkWash" cx="0" cy="0" r="1">
        <stop offset="0" stop-color="var(--pink-light)"/>
        <stop offset="0.55" stop-color="var(--pink)"/>
      </radialGradient>
    </defs>
    <rect width="608" height="860" fill="var(--pink)"/>
    <rect width="608" height="860" fill="url(#pinkWash)"/>
    <path d="M0,640 C150,545 380,462 608,436 L608,860 L0,860 Z" fill="var(--red)"/>
    <path d="M0,655 C150,560 380,477 608,451 L608,860 L0,860 Z" fill="var(--orange)"/>
    <path d="M0,670 C150,575 380,492 608,466 L608,860 L0,860 Z" fill="var(--white)"/>
    <g class="lookout-glass" fill="var(--white)">
      <circle cx="420" cy="178" r="88" fill="none" stroke="var(--white)" stroke-width="22"/>
      <circle cx="372" cy="120" r="14"/>
      <g transform="rotate(-22 470 330)">
        <rect x="456" y="270" width="28" height="30"/>
        <rect x="432" y="296" width="76" height="130" rx="16"/>
      </g>
    </g>
  </svg>

  <p class="headline headline--intro">We are on the…</p>
  <h1 class="headline headline--lookout">LOOKOUT</h1>
  <p class="headline headline--for">For a</p>

  <ul class="vacancies">
    <li class="vacancy">
      <svg class="vacancy-icon" viewBox="0 0 18 26"><circle cx="9" cy="7" r="6" fill="var(--white)" stroke="var(--ink)" stroke-width="2"/><rect x="6" y="13" width="6" height="12" rx="2" fill="var(--ink)"/></svg>
      <span>Operations and HR<br>Manager</span>
    </li>
    <li class="vacancy">
      <svg class="vacancy-icon" viewBox="0 0 18 26"><circle cx="9" cy="7" r="6" fill="var(--white)" stroke="var(--ink)" stroke-width="2"/><rect x="6" y="13" width="6" height="12" rx="2" fill="var(--ink)"/></svg>
      <span>Membership Advisor<br>(East Midlands)</span>
    </li>
    <li class="vacancy">
      <svg class="vacancy-icon" viewBox="0 0 18 26"><circle cx="9" cy="7" r="6" fill="var(--white)" stroke="var(--ink)" stroke-width="2"/><rect x="6" y="13" width="6" height="12" rx="2" fill="var(--ink)"/></svg>
      <span>Social Media Content<br>Creator</span>
    </li>
  </ul>

  <p class="tagline">THE UK’S FASTEST GROWING NETWORK FOR MANUFACTURERS</p>
  <p class="offices">OFFICES IN BIRMINGHAM AND LEEDS<br>- WE ARE AN INCLUSIVE EMPLOYER</p>

  <div class="partners">
    <span class="partner-badge partner-badge--green" role="img" aria-label="Regional partner badge"></span>
    <span class="partner-badge partner-badge--red" role="img" aria-label="Regional partner badge"></span>
  </div>

  <div class="inclusion-badge" role="img" aria-label="Inclusive employer badge"></div>
</main>
</body>
</html>
```